Business Card Design Project

We need a business card design for an existing company that we have just acquired and need to refresh and revamp to give it a fresher, more modern, and professional image.
We are a niche high end management consulting firm working with large BRQ300 type companies.
Our services include commercial advisory, change management, culture development, leadership and team development, and training.
The old website for this company is www.kelmorvo-grp.example that will give you a better understanding of what this business does.
However, we have updated the logo and are changing the website as well so your design for the business card might influence how we design the website.
Our corporate colours are red and white but we also use light grey, black, and dark blue (occasionally) on our stationery.
The final design should communicate partnership, creativity, performance, insight, and change.
Updates

Some of you were having trouble viewing the original logo file.  I have now updated another file with .jpg version of logo.  Hope this helps.

Target Market(s)

We are a consultancy firm servicing Top BRQ or Vantage 300 type companies.

Industry/Entity Type

Management Consulting

Requirements
Must have
• Design must have all contact information and logo on 1 side of card. Back of card should be solid colour or watermarked only - i.e. no real writing on back of card.
Cards must be scannable by those new business card scanners that store the image electronically.
Will be printing on high quality paper with matte finish so design must be high definition to allow good printing.
Card must be normal business card size (no small or 3/4 sized cards).
Nice to have
• A design that has a bit of 'movement' in it rather than look blockish and rigid. Not sure how this can be done but something that gives the card a sense of flow because our work all about integrating and synthesising the 'hard' commercial aspects with the 'soft' human (psychological) dimensions into contracts and projects.
Design should be transferrable to stationery and website to the extent possible/sensible.
Should not have
• - 'old fashioned' or 'girly' or 'comical' fonts.

- no clip art like images

- no superfluous design features that convey no real message or idea.

```html
<!DOCTYPE html>
<html lang="en">
<head>
<meta charset="utf-8">
<title>Kelmorvo Group – Business Cards</title>
<link href="https://fonts.googleapis.com/css2?family=Dosis:wght@300;400;600;700&display=swap" rel="stylesheet">
<style>
  :root {
    --brand-red: #a51d22;
    --wave-light: #f3d4d1;
    --wave-mid: #e7b0ab;
    --wave-edge: #e39d96;
    --card-white: #ffffff;
    --ink: #333333;
    --stage: #3b3b3b;
  }
  * { box-sizing: border-box; margin: 0; padding: 0; }
  html, body { width: 1200px; height: 848px; overflow: hidden; }
  body { background: var(--stage); font-family: "Dosis", sans-serif; position: relative; }

  .card {
    position: absolute; width: 363px; height: 222px;
    background: var(--card-white); overflow: hidden;
  }
  .card--front-a { left: 178px; top: 152px; }
  .card--front-b { left: 654px; top: 152px; }
  .card--back-a  { left: 178px; top: 392px; }
  .card--back-b  { left: 654px; top: 392px; }

  .wave-pattern { position: absolute; left: 0; top: 0; width: 363px; height: 222px; }

  .brand-mark {
    position: absolute; background: var(--brand-red);
    display: flex; align-items: center; justify-content: center;
    color: var(--card-white); font-weight: 700; letter-spacing: 0.5px;
    text-transform: uppercase; text-align: center; line-height: 1.05;
  }
  .brand-mark--rounded { border-radius: 14px; }
  .card--front-a .brand-mark, .card--front-b .brand-mark {
    left: 44px; top: 58px; width: 116px; height: 116px; font-size: 17px;
  }
  .card--back-a .brand-mark, .card--back-b .brand-mark {
    left: 19px; top: 15px; width: 90px; height: 92px; font-size: 13px;
  }

  .tagline {
    position: absolute; color: var(--brand-red); font-weight: 700;
    text-transform: uppercase; letter-spacing: 0.5px; line-height: 1;
    white-space: nowrap;
  }
  .card--front-a .tagline, .card--front-b .tagline { left: 176px; font-size: 30px; }
  .tagline--first  { top: 74px; }
  .tagline--second { top: 105px; }
  .tagline--third  { top: 136px; }
  .card--back-a .tagline, .card--back-b .tagline { font-size: 23px; }
  .card--back-a .tagline--first, .card--back-b .tagline--first { left: 132px; top: 28px; }
  .card--back-a .tagline--second, .card--back-b .tagline--second { left: 178px; top: 53px; }
  .card--back-a .tagline--third, .card--back-b .tagline--third { left: 215px; top: 78px; }

  .person-name {
    position: absolute; left: 19px; top: 121px; color: var(--brand-red);
    font-size: 15px; font-weight: 600; letter-spacing: 0.3px; text-transform: uppercase;
  }
  .person-title {
    position: absolute; right: 18px; top: 125px; color: var(--ink);
    font-size: 11.5px; font-weight: 400; text-transform: uppercase;
  }
  .rule { position: absolute; left: 19px; right: 18px; top: 142px; height: 1.5px; background: var(--brand-red); }

  .contact-list { position: absolute; list-style: none; font-size: 11.5px; color: var(--ink); font-weight: 400; line-height: 16.5px; }
  .contact-list--left { left: 17px; top: 149px; }
  .contact-list--right { left: 218px; top: 149px; }
  .contact-list li { display: flex; }
  .contact-list .key { color: var(--brand-red); width: 17px; flex: none; font-weight: 300; }
  .contact-list--right .key { width: 20px; }
</style>
</head>
<body>

<svg width="0" height="0" style="position:absolute" aria-hidden="true">
  <defs>
    <linearGradient id="waveFill" x1="0" y1="0" x2="1" y2="0">
      <stop offset="0" stop-color="#e7b0ab" stop-opacity="0.7"/>
      <stop offset="0.5" stop-color="#f3d4d1" stop-opacity="0.6"/>
      <stop offset="1" stop-color="#e39d96" stop-opacity="0.8"/>
    </linearGradient>
  </defs>
</svg>

<section class="card card--front-a">
  <svg class="wave-pattern" viewBox="0 0 363 222" role="img" aria-label="Flowing red line wave pattern">
    <path d="M0 120 C60 60 120 50 180 90 S300 110 363 60 L363 170 C300 150 240 140 180 130 S60 170 0 150 Z" fill="url(#waveFill)"/>
  </svg>
  <div class="brand-mark">Kelmorvo<br>Group</div>
  <div class="tagline tagline--first">Advise</div>
  <div class="tagline tagline--second">Evolve</div>
  <div class="tagline tagline--third">Transform</div>
</section>

<section class="card card--front-b">
  <svg class="wave-pattern" viewBox="0 0 363 222" role="img" aria-label="Flowing red line wave pattern">
    <path d="M0 120 C60 60 120 50 180 90 S300 110 363 60 L363 170 C300 150 240 140 180 130 S60 170 0 150 Z" fill="url(#waveFill)"/>
  </svg>
  <div class="brand-mark brand-mark--rounded">Kelmorvo<br>Group</div>
  <div class="tagline tagline--first">Advise</div>
  <div class="tagline tagline--second">Evolve</div>
  <div class="tagline tagline--third">Transform</div>
</section>

<section class="card card--back-a">
  <svg class="wave-pattern" viewBox="0 0 363 222" role="img" aria-label="Flowing red line wave pattern">
    <path d="M0 30 C80 0 160 20 220 50 S320 40 363 10 L363 110 C300 100 250 110 200 100 S80 60 0 70 Z" fill="url(#waveFill)"/>
  </svg>
  <div class="brand-mark">Kelmorvo<br>Group</div>
  <div class="tagline tagline--first">Advise</div>
  <div class="tagline tagline--second">Evolve</div>
  <div class="tagline tagline--third">Transform</div>
  <div class="person-name">Tom Harwell</div>
  <div class="person-title">Partner - Head of Advisory Services</div>
  <div class="rule"></div>
  <ul class="contact-list contact-list--left">
    <li><span class="key">M</span>+61 (0)400 555 018</li>
    <li><span class="key">P</span>+61 3 9000 2214</li>
    <li><span class="key">F</span>+61 3 9000 2210</li>
    <li><span class="key">E</span>tom.harwell@kelmorvo.example</li>
  </ul>
  <ul class="contact-list contact-list--right">
    <li><span class="key">W</span>www.kelmorvo.example</li>
    <li><span class="key">A</span>Level 6, 120 Harbour Rd,</li>
    <li><span class="key"></span>Carlton, Vic 3053,</li>
    <li><span class="key"></span>Australia</li>
  </ul>
</section>

<section class="card card--back-b">
  <svg class="wave-pattern" viewBox="0 0 363 222" role="img" aria-label="Flowing red line wave pattern">
    <path d="M0 30 C80 0 160 20 220 50 S320 40 363 10 L363 110 C300 100 250 110 200 100 S80 60 0 70 Z" fill="url(#waveFill)"/>
  </svg>
  <div class="brand-mark brand-mark--rounded">Kelmorvo<br>Group</div>
  <div class="tagline tagline--first">Advise</div>
  <div class="tagline tagline--second">Evolve</div>
  <div class="tagline tagline--third">Transform</div>
  <div class="person-name">Tom Harwell</div>
  <div class="person-title">Partner - Head of Advisory Services</div>
  <div class="rule"></div>
  <ul class="contact-list contact-list--left">
    <li><span class="key">M</span>+61 (0)400 555 018</li>
    <li><span class="key">P</span>+61 3 9000 2214</li>
    <li><span class="key">F</span>+61 3 9000 2210</li>
    <li><span class="key">E</span>tom.harwell@kelmorvo.example</li>
  </ul>
  <ul class="contact-list contact-list--right">
    <li><span class="key">W</span>www.kelmorvo.example</li>
    <li><span class="key">A</span>Level 6, 120 Harbour Rd,</li>
    <li><span class="key"></span>Carlton, Vic 3053,</li>
    <li><span class="key"></span>Australia</li>
  </ul>
</section>

</body>
</html>
```